Book Cover for our New Book for teachers

We would like a book cover designed. This book is a collection of 23 different chapters on various topics. Each topic is something that a teacher should know about in order to teach kids effectively. It is a collection of thoughts on the problems facing teachers, and how to overcome those problems. I have attached a Microsoft Word document that details our project requests.
Target Market(s)
Education/Teachers
Industry/Entity Type
Education
Font styles to use
Other font styles liked:
- UP TO YOUR JUDGMENT
Colors
Designer to choose colors to be used in the design.
Requirements
Must have
- Great design
Nice to have
- Colors, elegant fonts, classy...YET professional....
Should not have
- "KID" or child fonts, or "chalk fonts" or anything like that. this book is for PROFESSIONALS.

```html
<!DOCTYPE html>
<html lang="en">
<head>
<meta charset="UTF-8">
<title>Evidence-Driven Practices to Build Classroom Success — Book Cover</title>
<link href="https://fonts.googleapis.com/css2?family=Roboto:wght@300;900&family=PT+Sans:wght@400&display=swap" rel="stylesheet">
<style>
  :root {
    --backdrop: #ece8e1;
    --paper: #ffffff;
    --accent-green: #0ea556;
    --edge-shadow: #4a4a4a;
    --ink: #1f1f1f;
    --ink-soft: #2e2e2e;
    --shelf-dark: #3a3d42;
    --shelf-mid: #5b5f66;
  }
  * { margin: 0; padding: 0; box-sizing: border-box; }
  html, body {
    width: 1200px;
    height: 730px;
    overflow: hidden;
    background: var(--backdrop);
  }
  .stage {
    position: relative;
    width: 1200px;
    height: 730px;
  }
  .book-cover {
    position: absolute;
    left: 373px;
    top: 25px;
    width: 454px;
    height: 680px;
    background: var(--paper);
    overflow: hidden;
    box-shadow: 0 6px 18px rgba(0,0,0,0.18);
  }
  .cover-shapes {
    position: absolute;
    inset: 0;
    width: 100%;
    height: 100%;
  }
  .cover-title {
    position: absolute;
    top: 182px;
    left: 0;
    width: 100%;
    text-align: center;
    color: var(--ink);
    font-family: "Roboto", Arial, sans-serif;
    line-height: 1;
  }
  .cover-title .line-strong {
    display: block;
    font-weight: 900;
    font-size: 30px;
    letter-spacing: -0.2px;
  }
  .cover-title .line-light {
    display: block;
    font-weight: 300;
    font-size: 27px;
    margin: 2px 0 3px;
    letter-spacing: 0.2px;
  }
  .shelf-art {
    position: absolute;
    left: 28px;
    top: 330px;
    width: 398px;
    height: 150px;
    background: linear-gradient(90deg,
      var(--shelf-dark) 0%, #2d4f8e 14%, #c8232c 24%, var(--shelf-mid) 34%,
      #e3b21c 44%, #3b3f6e 54%, #d35a1f 64%, var(--shelf-dark) 74%,
      #c0b247 86%, #2f5a3a 100%);
    opacity: 0.9;
  }
  .cover-tagline {
    position: absolute;
    right: 42px;
    top: 500px;
    text-align: right;
    font-family: "PT Sans", Arial, sans-serif;
    font-size: 17px;
    line-height: 1.22;
    color: var(--ink-soft);
  }
</style>
</head>
<body>
  <main class="stage">
    <section class="book-cover">
      <svg class="cover-shapes" viewBox="0 0 454 680" aria-hidden="true">
        <polygon points="30,0 454,0 454,152" fill="var(--edge-shadow)"/>
        <polygon points="40,0 454,0 454,146" fill="var(--accent-green)"/>
        <polygon points="0,498 0,680 440,680" fill="var(--edge-shadow)"/>
        <polygon points="0,505 0,680 430,680" fill="var(--accent-green)"/>
      </svg>

      <h1 class="cover-title">
        <span class="line-strong">EVIDENCE-DRIVEN</span>
        <span class="line-light">PRACTICES TO BUILD</span>
        <span class="line-strong">CLASSROOM SUCCESS</span>
      </h1>

      <div class="shelf-art" role="img" aria-label="Row of upright books on a shelf with colourful spines, each titled with an education topic"></div>

      <p class="cover-tagline">
        Insights &amp; Strategies from 23<br>
        Classroom Teachers, Principals<br>
        School Executives &amp; More!
      </p>
    </section>
  </main>
</body>
</html>
```